Business Card/Logo Design Project

Design the Business card For a psychologist providing relationship workshops, see website draft at www.brightmorrowtalks.com.au.

The background is to be beige with shadows in ivory of the letter "L" as shown on the website noted above.

The words "Kindred Hours" on the front with the first letter of each word in very scrolled lettering and the remaining letters more formal. The front design is to be the logo of the business for use on other items.

The reverse is to show...

client's name
date
time
workshop number
workshop name
and at the bottom "PLEASE BE PUNCTUAL. BRING NOTEPAD & PEN"

Target Market(s)

female, middle-class, educated, introspective

Industry/Entity Type

Business

Requirements
Must have
• see www.brightmorrowtalks.com.au for the design aesthetic - just need you to make it look professional.

cream, beige, grey, chocolate, tan, ivory.

calligraphy shadows as per referenced website

business card back, flyer and postcard to just be background so that I can add text on top through papercrane.

see website for colour-scheme.
Should not have
• not cutesy, pink, or mushy

```html
<!DOCTYPE html>
<html lang="en">
<head>
<meta charset="utf-8">
<title>Kindred Hours – Appointment Card</title>
<link rel="stylesheet" href="https://fonts.googleapis.com/css2?family=Sorts+Mill+Goudy&display=swap">
<style>
  :root {
    --card-beige: #c3ac7c;
    --flourish-tan: #a8905f;
    --flourish-light: #b59d6c;
    --title-brown: #3d2c13;
    --label-brown: #5a4829;
    --footer-brown: #5f4b26;
    --rule-ivory: #e6d9b6;
  }
  * { box-sizing: border-box; margin: 0; padding: 0; }
  html, body {
    width: 1200px;
    height: 734px;
    overflow: hidden;
    background: var(--card-beige);
  }
  .card {
    position: relative;
    width: 1200px;
    height: 734px;
    background: var(--card-beige);
    overflow: hidden;
    font-family: "Sorts Mill Goudy", "Goudy Old Style", Georgia, serif;
  }
  .flourish {
    position: absolute;
    pointer-events: none;
  }
  .flourish--left {
    left: -60px;
    top: -80px;
    width: 900px;
    height: 820px;
    background: radial-gradient(ellipse at 45% 40%, rgba(168,144,95,0.55) 0%, rgba(168,144,95,0.25) 45%, rgba(195,172,124,0) 72%);
  }
  .flourish--right {
    left: 760px;
    top: 230px;
    width: 480px;
    height: 520px;
    background: radial-gradient(ellipse at 50% 40%, rgba(181,157,108,0.6) 0%, rgba(168,144,95,0.3) 45%, rgba(195,172,124,0) 72%);
  }
  .card__title {
    position: absolute;
    left: 0;
    width: 1200px;
    top: 44px;
    text-align: center;
    font-size: 52px;
    font-weight: 400;
    color: var(--title-brown);
    letter-spacing: 0.5px;
  }
  .field-label {
    position: absolute;
    font-size: 48px;
    color: var(--label-brown);
    line-height: 1;
    white-space: nowrap;
  }
  .field-line {
    position: absolute;
    height: 0;
    border-bottom: 3px dotted var(--rule-ivory);
  }
  .label--client   { left: 59px;  top: 164px; }
  .line--client    { left: 348px; width: 795px; top: 198px; }
  .label--dates    { left: 59px;  top: 281px; }
  .line--dates     { left: 220px; width: 499px; top: 315px; }
  .label--time     { left: 736px; top: 281px; }
  .line--time      { left: 864px; width: 279px; top: 315px; }
  .label--workshop { left: 59px;  top: 397px; }
  .line--workshop  { left: 573px; width: 570px; top: 433px; }
  .line--extra     { left: 59px;  width: 1084px; top: 552px; }
  .card__footer {
    position: absolute;
    left: 0;
    width: 1200px;
    top: 624px;
    text-align: center;
    font-size: 46px;
    color: var(--footer-brown);
    white-space: nowrap;
  }
</style>
</head>
<body>
  <section class="card">
    <div class="flourish flourish--left" role="img" aria-label="Large faint calligraphic letter flourish in tan"></div>
    <div class="flourish flourish--right" role="img" aria-label="Faint calligraphic spiral flourish in tan"></div>

    <h1 class="card__title">Appointment/Workshop</h1>

    <span class="field-label label--client">Client Name</span>
    <span class="field-line line--client"></span>

    <span class="field-label label--dates">Date(s)</span>
    <span class="field-line line--dates"></span>
    <span class="field-label label--time">Time</span>
    <span class="field-line line--time"></span>

    <span class="field-label label--workshop">Workshop No’ &amp; Name</span>
    <span class="field-line line--workshop"></span>
    <span class="field-line line--extra"></span>

    <p class="card__footer">Please be Panctual. Bring a Notepad &amp; Pen</p>
  </section>
</body>
</html>
```